Cover for "ROOTED! The skill and rhythm of guiding teams through calm and delight"

My first book for a global audience of modern performance leaders needs its cover!
I am an international executive coach and I've developed a new approach to replace classic Performance Management with a natural, sustainable approach fit for human beings :) My first book is about this approach and serves two purposes: helping leaders and sparking their curiosity to learn more, and positioning myself as a thought leader in the field.
The book is built on personal experience; it is both professional and personal ("From me to You"), and I'd like to position it beyond classic categorisation.
Its cover should communicate humanness, naturalness, ease and joy, within an unmistakably business-y context. I would like to see designs that use the color yellow (but not sure it communicates the right things).
Updates

Target Market(s)

Leaders who aspire to have a positive impact and deliver results in a meaningful way

Industry/Entity Type

Consulting & Executive Coaching - Trusted Advisor

Font styles to use
Other font styles liked:
• Helvetica Neue

Colors
0094D4
00A9DD
6FCCEA
C7EBF8
E9F6FB
FFC000
F8CF3A
FAE287
FDF2CF
FEFAEE
EE7325
F08F49
F5BC92
FAE3D3
FDF4ED

Requirements
Must have
• A both-and feeling to it (see description), e.g., masculine AND feminine, business AND humanness. Power with, not power over...
Should not have
• Too much "bling" - no classic status symbol business success language

```html
<!DOCTYPE html>
<html lang="en">
<head>
<meta charset="utf-8">
<title>ROOTED! – Book Cover Spread</title>
<link rel="stylesheet" href="https://fonts.googleapis.com/css2?family=Playfair+Display:wght@400&family=Poppins:wght@400;600;700&display=swap">
<style>
  :root {
    --stage: #3d6690;
    --back-cover: #355b82;
    --back-cover-deep: #2c4d70;
    --accent: #f0445f;
    --white: #ffffff;
    --ink-soft: #f2f4f7;
    --sea-deep: #1f4a63;
    --sea-mid: #2f7a86;
    --sea-light: #6fa6b0;
    --sea-foam: #c9dde0;
  }
  * { box-sizing: border-box; margin: 0; padding: 0; }
  html, body { width: 1200px; height: 899px; overflow: hidden; }
  body { background: var(--stage); position: relative; font-family: "Poppins", sans-serif; }

  .book {
    position: absolute; left: 82px; top: 84px; width: 1035px; height: 730px;
    box-shadow: 0 14px 30px rgba(10, 25, 45, 0.45);
    overflow: hidden;
  }

  /* Back cover */
  .back-cover {
    position: absolute; left: 0; top: 0; width: 487px; height: 730px;
    background: linear-gradient(90deg, var(--back-cover) 0%, var(--back-cover) 85%, var(--back-cover-deep) 100%);
  }
  .author-portrait {
    position: absolute; left: 0; top: 0; width: 190px; height: 242px;
    background: radial-gradient(ellipse at 45% 45%, #b8b8b8 0%, #9a9a9a 55%, #7c7c7c 100%);
  }
  .back-author {
    position: absolute; left: 216px; top: 106px;
    font-weight: 700; font-size: 19px; line-height: 26px; color: var(--white); letter-spacing: -0.2px;
  }
  .accent-rule {
    position: absolute; left: 45px; top: 242px; width: 398px; height: 12px; background: var(--accent);
  }
  .back-title {
    position: absolute; left: 45px; top: 263px;
    font-family: "Playfair Display", serif; font-weight: 400; font-size: 68px; line-height: 1;
    letter-spacing: 0.25em; color: var(--white); white-space: nowrap;
    transform: scaleX(0.72); transform-origin: left top;
  }
  .back-subtitle {
    position: absolute; left: 45px; top: 350px; width: 165px;
    font-weight: 700; font-size: 11.5px; line-height: 16.5px; color: var(--accent);
  }
  .back-blurb {
    position: absolute; left: 216px; top: 351px; width: 206px; height: 326px; overflow: hidden;
    font-size: 9.8px; line-height: 13.5px; color: var(--ink-soft);
    hyphens: auto; -webkit-hyphens: auto;
  }
  .code-panel {
    position: absolute; left: 45px; top: 482px; width: 76px; height: 200px; background: var(--white);
  }

  /* Sea photograph across spine and front */
  .sea-photo {
    position: absolute; left: 487px; top: 0; width: 548px; height: 730px;
    background:
      radial-gradient(ellipse at 70% 20%, rgba(201,221,224,0.55) 0%, rgba(201,221,224,0) 45%),
      radial-gradient(ellipse at 40% 60%, rgba(201,221,224,0.45) 0%, rgba(201,221,224,0) 40%),
      linear-gradient(175deg, var(--sea-light) 0%, var(--sea-mid) 35%, var(--sea-deep) 70%, #2b5f86 100%);
  }
  .spine-veil {
    position: absolute; left: 487px; top: 0; width: 61px; height: 730px; background: rgba(255,255,255,0.12);
  }

  /* Spine */
  .spine-title-block {
    position: absolute; left: 487px; top: 0; width: 61px; height: 163px;
    background: var(--back-cover);
  }
  .spine-title {
    position: absolute; left: 17px; top: 21px; width: 28px;
    writing-mode: vertical-rl; white-space: nowrap;
    font-family: "Playfair Display", serif; font-size: 30px; line-height: 28px;
    letter-spacing: 0.3em; color: var(--white);
    transform: scaleY(0.62); transform-origin: center top;
  }
  .spine-subtitle {
    position: absolute; left: 506px; top: 163px; width: 23px; height: 363px;
    background: var(--accent); writing-mode: vertical-rl;
    font-weight: 700; font-size: 10px; line-height: 23px; color: var(--white); padding-top: 8px;
    white-space: nowrap;
  }
  .spine-author {
    position: absolute; left: 506px; top: 561px; width: 23px;
    writing-mode: vertical-rl; white-space: nowrap;
    font-weight: 700; font-size: 18px; line-height: 23px; color: var(--white);
  }

  /* Front cover */
  .front-title-art { position: absolute; left: 548px; top: 0; width: 487px; height: 730px; }
  .front-title-word { font-family: "Playfair Display", serif; fill: var(--white); fill-opacity: 0.94; }
  .front-author {
    position: absolute; left: 674px; top: 104px;
    font-weight: 700; font-size: 31px; line-height: 46px; color: var(--white); letter-spacing: -0.3px;
  }
  .front-subtitle-panel {
    position: absolute; left: 660px; top: 196px; width: 265px; height: 106px;
    background: var(--accent);
    display: flex; align-items: center; justify-content: center; text-align: center;
    font-weight: 700; font-size: 13.8px; line-height: 20px; color: var(--white);
  }
</style>
</head>
<body>
  <div class="book">
    <section class="back-cover">
      <div class="author-portrait" role="img" aria-label="Black and white portrait of the author, arms crossed, smiling"></div>
      <p class="back-author">Marta Solberg</p>
      <div class="accent-rule"></div>
      <h2 class="back-title">ROOTED!</h2>
      <p class="back-subtitle">The Skill and Rhythm<br>of Guiding Teams<br>through Calm and Delight</p>
      <p class="back-blurb">Vivamus ut sapien tristique, consequat lorem eu, pulvinar risus. Duis maximus tristique metus quis volutpat. Sed ornare, erat vel efficitur vulputate, mauris mi venenatis purus, et laoreet libero ligula nec massa. Class aptent taciti sociosqu ad litora torquent per conubia nostra, per inceptos himenaeos. Proin vel felis massa. Pellentesque commodo diam eu ipsum aliquet, ac pellentesque purus maximus. Donec sollicitudin odio quis purus mattis blandit. Fusce dignissim scelerisque egestas. Integer rutrum, odio ac feugiat molestie, lectus dolor elementum metus, ut mattis urna leo in urna. Suspendisse at egestas orci. Donec eleifend est lorem, id volutpat dui facilisis in. Cras nisi libero, condimentum quis est non, feugiat tincidunt nulla. Donec fermentum elementum velit, eget iaculis velit. Nulla ultricies vitae sem sed fringilla. Nullam volutpat bibendum erat sed finibus. Quisque semper dictum gravida.</p>
      <div class="code-panel"></div>
    </section>

    <div class="sea-photo" role="img" aria-label="Photograph of a rowing crew in a four-person boat on rough, foaming ocean waves"></div>
    <div class="spine-veil"></div>

    <div class="spine-title-block"><span class="spine-title">ROOTED!</span></div>
    <div class="spine-subtitle">The Skill and Rhythm of Guiding Teams through Calm and Delight</div>
    <div class="spine-author">Marta Solberg</div>

    <svg class="front-title-art" viewBox="0 0 487 730" role="img" aria-label="ROOTED!">
      <g transform="translate(30 21) rotate(90)">
        <text class="front-title-word" x="0" y="0" font-size="165" textLength="675" lengthAdjust="spacingAndGlyphs">ROOTED!</text>
      </g>
    </svg>

    <p class="front-author">Marta Solberg</p>
    <div class="front-subtitle-panel">The Skill and Rhythm<br>of Guiding Teams<br>through Calm and Delight</div>
  </div>
</body>
</html>
```